Hi Performance Vehicle Import business needs a Business card

Velocrest Is a Melbourne based company importing and complying Japanese,American and European vehicles. We are expanding our company to a bigger factory in hopes to also expand our client base.

currently on our business cards we are advertising for the following
-Japanese, American and European vehicle importers
-ADR Compliance
-Direct import solutions
-Vehicle sales
-General maintenance

What we would like, is for customers to understand what we specialize in and be able to communicate with them by just looking at our business card.

We also have attached our current logo and previous cards with look outdated at the moment.

Target Market(s)

We are specializing in special enthusiast vehicles and only target a niche market as Imports in Australia are not very popular so we need to get our massage to everyone whos out there interested in such vehicles. We currently import Korvath Stratline Zrx's, Tarrendo Vex, Brantley Outriders, Velmoretti's , Halvick Broncats, Torvella's and Castoni and Rizzo's near future.We are targeting younger generation as well as mature crowd bit of everyone..

Industry/Entity Type

Advertising

Requirements
Must have
• Lets look at few designs and we will work with the designer once preferable design has been selected.
Nice to have
• We would like to see something in the back ground to represent the automotive field. Bring your creativity so we might change our mind. We still like to keep the existing logo.
Should not have
• The business cards attached are from our local designer. We think they are outdated,wrong fonts and arrangement of the information is not quite right. So we would like to see something totally different.

```html
<!DOCTYPE html>
<html lang="en">
<head>
<meta charset="utf-8">
<title>Velocrest Business Card</title>
<link href="https://fonts.googleapis.com/css2?family=Roboto+Condensed:wght@400;700&family=Roboto:wght@400;500&display=swap" rel="stylesheet">
<style>
  :root {
    --page-bg: #e9e7e4;
    --card-dark: #0d1118;
    --card-mid: #1f2a38;
    --brand-red: #d4161f;
    --red-deep: #7c0a10;
    --silver: #d9dde2;
    --text-light: #f2f2f2;
    --text-muted: #c9ccd1;
    --bullet: #9aa0a8;
    --car-tone: #4b5058;
  }
  * { margin: 0; padding: 0; box-sizing: border-box; }
  html, body { width: 1200px; height: 469px; overflow: hidden; background: var(--page-bg); }
  .canvas { position: relative; width: 1200px; height: 469px; }
  .card {
    position: absolute; top: 54px; width: 498px; height: 360px; overflow: hidden;
    background: radial-gradient(ellipse at 55% 35%, var(--card-mid) 0%, var(--card-dark) 70%);
    box-shadow: 0 6px 18px rgba(0,0,0,0.35);
    font-family: "Roboto", sans-serif; color: var(--text-light);
  }
  .card--front { left: 106px; }
  .card--back { left: 608px; }
  .card-shape { position: absolute; inset: 0; width: 100%; height: 100%; }

  .brand { position: absolute; }
  .brand-name {
    font-family: "Roboto Condensed", sans-serif; font-weight: 700;
    color: var(--text-light); letter-spacing: 2px; line-height: 1;
  }
  .brand-url { position: absolute; font-size: 9px; color: var(--text-muted); letter-spacing: 0.5px; }
  .brand-tagline {
    font-family: "Roboto Condensed", sans-serif; font-weight: 700;
    font-size: 8.5px; letter-spacing: 0.6px; color: var(--text-light); margin-top: 6px;
  }
  .card--front .brand { left: 60px; top: 48px; }
  .card--front .brand-name { font-size: 44px; }
  .card--front .brand-url { left: 230px; top: -16px; }

  .card--back .brand { right: 26px; top: 28px; text-align: right; }
  .card--back .brand-name { font-size: 26px; }
  .card--back .brand-url { right: 0; top: -12px; font-size: 7px; }

  .contact-list { position: absolute; left: 30px; top: 140px; list-style: none; font-size: 13px; line-height: 19px; }
  .contact-list b { display: inline-block; width: 16px; font-weight: 500; }
  .address { position: absolute; left: 30px; top: 255px; font-size: 13px; line-height: 19px; color: var(--text-light); }
  .person-name {
    position: absolute; left: 236px; top: 263px;
    font-family: "Roboto Condensed", sans-serif; font-weight: 700; font-size: 19px; letter-spacing: 1px;
  }

  .service-list { position: absolute; left: 28px; top: 28px; list-style: none; font-size: 15px; line-height: 19px; }
  .service-list li { position: relative; padding-left: 22px; margin-bottom: 4.5px; }
  .service-list li::before {
    content: ""; position: absolute; left: 0; top: 4px; width: 11px; height: 11px; border-radius: 50%;
    background: radial-gradient(circle at 35% 35%, #e3e5e8, var(--bullet) 70%);
  }
  .car-photo {
    position: absolute; right: 0; top: 150px; width: 300px; height: 180px;
    background: radial-gradient(ellipse at 55% 55%, var(--car-tone) 0%, #2a2e35 55%, rgba(13,17,24,0) 75%);
  }
  .abn { position: absolute; left: 20px; top: 245px; font-size: 8px; color: var(--text-light); }
</style>
</head>
<body>
<main class="canvas">

  <section class="card card--front">
    <svg class="card-shape" viewBox="0 0 498 360" aria-hidden="true">
      <defs>
        <linearGradient id="redBand" x1="0" y1="0" x2="1" y2="1">
          <stop offset="0" stop-color="#b3121a"/>
          <stop offset="0.5" stop-color="#e11b24"/>
          <stop offset="1" stop-color="#7c0a10"/>
        </linearGradient>
        <linearGradient id="silverEdge" x1="0" y1="0" x2="1" y2="0">
          <stop offset="0" stop-color="#6d737b"/>
          <stop offset="0.45" stop-color="#ffffff"/>
          <stop offset="1" stop-color="#8a9099"/>
        </linearGradient>
      </defs>
      <path d="M0,118 C160,128 320,160 498,205 L498,360 L0,360 Z" fill="url(#redBand)"/>
      <path d="M0,112 C160,122 320,152 498,198" fill="none" stroke="url(#silverEdge)" stroke-width="5"/>
      <path d="M0,106 C160,116 320,146 498,192" fill="none" stroke="#05070a" stroke-width="3"/>
    </svg>
    <div class="brand">
      <span class="brand-url">VELOCREST.COM.AU</span>
      <div class="brand-name">VELOCREST</div>
      <div class="brand-tagline">HIGH PERFORMANCE VEHICLE IMPORTERS</div>
    </div>
    <ul class="contact-list">
      <li><b>T</b>: 0400 518 274</li>
      <li><b>F</b>: 03 9000 4127</li>
      <li><b>E</b>: sales@velocrest.com.au</li>
      <li><b>W</b>: velocrest.com.au</li>
    </ul>
    <p class="address">Factory 4/210 Elmstone Road,<br>Dandenong South Vic 3175</p>
    <p class="person-name">KAVEEN MORATHENNA</p>
  </section>

  <section class="card card--back">
    <svg class="card-shape" viewBox="0 0 498 360" aria-hidden="true">
      <defs>
        <linearGradient id="redBandBack" x1="0" y1="0" x2="1" y2="0">
          <stop offset="0" stop-color="#c3141d"/>
          <stop offset="0.5" stop-color="#e11b24"/>
          <stop offset="1" stop-color="#7c0a10"/>
        </linearGradient>
        <linearGradient id="silverEdgeBack" x1="0" y1="0" x2="1" y2="0">
          <stop offset="0" stop-color="#7a8088"/>
          <stop offset="0.5" stop-color="#ffffff"/>
          <stop offset="1" stop-color="#8a9099"/>
        </linearGradient>
      </defs>
      <path d="M0,222 C140,232 300,270 498,330 L498,360 L0,360 Z" fill="url(#redBandBack)"/>
      <path d="M0,216 C140,226 300,262 498,322" fill="none" stroke="url(#silverEdgeBack)" stroke-width="4"/>
      <path d="M0,211 C140,221 300,256 498,316" fill="none" stroke="#05070a" stroke-width="3"/>
    </svg>
    <ul class="service-list">
      <li>Japanese, American &amp;<br>European Vehicle Importers</li>
      <li>ADR Compliance</li>
      <li>Direct import solutions</li>
      <li>Vehicle sales</li>
      <li>General maintenance</li>
    </ul>
    <div class="brand">
      <span class="brand-url">VELOCREST.COM.AU</span>
      <div class="brand-name">VELOCREST</div>
    </div>
    <div class="car-photo" role="img" aria-label="Photo of a dark grey sports car, three-quarter front view"></div>
    <p class="abn">ABN: 52600418297</p>
  </section>

</main>
</body>
</html>
```